Postcard Design

Company Name--motion harbor
482 Garnet Avenue
Brooklyn New York11231
347-555-0182
www.motionharbors. example
We are a boutique personal fitness company in a exclusive neighnorhood in Brooklyn New York. We specialize in personal training and innovate new fitness classes such as Pulse-Circuit QVR and Tabata.

We want our brand to be high-end but open to all. Laid-back but experts in the field of fitness. Innovative and flexible. Proffessional, friendly and inspiring.

Personal attention for our clients is a must as well as making sure they succeed. 87% of our clients reach their goals.

Colors should be bright but sophisticated with a little aggression but not intimidation.
Updates

Company Name-And contact info has been updated on the brief

I posted a logo. And the colors on the website have changed. If you could incorporate the website color scheme that would be helpful. If for whatever reason the logo is not here I will try to upload again.

Change the contact info: www.motionharbors.example You tube: Brisco and the Motion Harbor Email: Motionharbors@mailbox.example Verbiage changes: 'The only boutique personal fitness studio in Brooklyn. Featuring uniquely proprietary classes QVR, Cross Training and now Tabata." Verbiage Additions Safe for moms, dads and we offer enhanced childcare with certified child care development teachers with our partner studios. Classes start at $15

Please Add : Use this postcard to receive 10% any service

Hi, I could not upload the logo. However they said that our Logo should be uploaded now as I sent it to them manually.

Target Market(s)

30-40 year old women and new moms looking to do cross fit and personal training. Income 80-85K.

Industry/Entity Type

Boutique

Requirements
Must have
• Highlight Tabata and the excellence of the classes.Tag lines- Increase calorie burn by 20%. Increase muscle tone by 25%.Increase metabolism by 25%. Classes only available by appointment. 30mins or 1 hour.
Nice to have
• Attractive and fit young people having fun. Personal training.
Should not have
• Overly sexual fitness models.

```html
<!DOCTYPE html>
<html lang="en">
<head>
<meta charset="utf-8">
<title>Motion Harbor Postcard</title>
<link href="https://fonts.googleapis.com/css2?family=Open+Sans:ital,wght@0,400;0,600;0,700;1,400;1,700;1,800&family=Roboto+Condensed:wght@400;700&display=swap" rel="stylesheet">
<style>
  :root {
    --red: #d42a2e;
    --red-dark: #9e1b1f;
    --charcoal: #2b2b2d;
    --teal: #1f8f9a;
    --grey-text: #3a3a3a;
    --paper: #ffffff;
    --canvas: #e9e9e9;
  }
  * { margin: 0; padding: 0; box-sizing: border-box; }
  html, body { width: 849px; height: 1200px; overflow: hidden; background: var(--canvas); }
  body { position: relative; font-family: "Open Sans", Arial, sans-serif; }

  .card { position: absolute; left: 48px; width: 753px; background: var(--paper); overflow: hidden; box-shadow: 0 2px 6px rgba(0,0,0,.18); }
  .card--front { top: 28px; height: 552px; }
  .card--back { top: 612px; height: 560px; }

  .shards { position: absolute; inset: 0; }

  .photo { position: absolute; }
  .photo--trainer { left: 0; top: 70px; width: 290px; height: 440px;
    background: radial-gradient(ellipse at 45% 45%, #d9b79b 0%, #b89277 35%, #e9e5e2 75%); }

  .title-band { position: absolute; left: 270px; top: 0; width: 483px; height: 160px; background: var(--red); padding: 24px 14px 0 14px; text-align: center; color: #fff; }
  .title-band h1 { font-style: italic; font-weight: 800; font-size: 28px; line-height: 1.2; letter-spacing: -0.4px; white-space: nowrap; }
  .title-band p { font-style: italic; font-size: 12px; margin-top: 10px; white-space: nowrap; }

  .stats { position: absolute; left: 310px; top: 198px; list-style: none; font-family: "Roboto Condensed", Arial, sans-serif; color: var(--charcoal); }
  .stats li { font-size: 33px; line-height: 46px; white-space: nowrap; }
  .stats b { font-weight: 700; font-size: 42px; margin-right: 6px; }

  .offer { position: absolute; right: -70px; top: 340px; width: 300px; height: 300px; border-radius: 50%; background: var(--teal); color: #fff; padding: 40px 0 0 58px; font-family: "Roboto Condensed", Arial, sans-serif; }
  .offer span { display: block; font-size: 19px; line-height: 22px; font-weight: 700; }
  .offer strong { display: block; font-size: 62px; line-height: 68px; margin-left: 20px; }

  .site { position: absolute; left: 290px; top: 482px; font-size: 14px; color: var(--charcoal); }

  .photo--group { left: 0; top: 0; width: 753px; height: 290px;
    background: linear-gradient(100deg, #8fa7b9 0%, #c8c2ba 40%, #e7e3df 70%, #cfd7dd 100%); }

  .goal-band { position: absolute; left: 0; top: 300px; width: 753px; height: 60px; background: var(--red); color: #fff; text-align: center; font-style: italic; font-size: 32px; line-height: 60px; font-weight: 400; }
  .goal-band b { font-weight: 700; font-size: 40px; }

  .blurb { position: absolute; left: 40px; top: 374px; width: 673px; text-align: center; color: var(--grey-text); font-size: 17px; line-height: 23px; }

  .contact { position: absolute; right: 40px; top: 450px; text-align: right; font-style: normal; font-weight: 700; font-size: 13px; line-height: 17px; color: var(--charcoal); }
  .contact h2 { font-size: 14px; font-weight: 700; line-height: 19px; }
</style>
</head>
<body>

<section class="card card--front">
  <svg class="shards" width="753" height="552" viewBox="0 0 753 552" aria-hidden="true">
    <polygon points="0,0 300,0 210,60 0,110" fill="#9e1b1f"/>
    <polygon points="0,0 240,0 0,70" fill="#d42a2e"/>
    <polygon points="270,160 753,160 753,190 520,184" fill="#2b2b2d"/>
    <polygon points="0,552 240,460 330,552" fill="#2b2b2d"/>
    <polygon points="0,552 0,500 160,552" fill="#d42a2e"/>
  </svg>
  <div class="photo photo--trainer" role="img" aria-label="Photo of a fit woman in a crouched stance lifting dumbbells"></div>
  <header class="title-band">
    <h1>The Only Boutique Personal<br>Fitness Studio In Brooklyn</h1>
    <p>Featuring uniquely proprietary classes QVR, Cross Training and Tabata</p>
  </header>
  <ul class="stats">
    <li><b>20%</b> Increase calorie burn</li>
    <li><b>25%</b> Increase muscle tone</li>
    <li><b>25%</b> Increase metabolism</li>
  </ul>
  <div class="offer"><span>USE THIS<br>POSTCARD &amp; GET</span><strong>10%</strong></div>
  <p class="site">www.motionharbors.example</p>
</section>

<section class="card card--back">
  <div class="photo photo--group" role="img" aria-label="Photo of a group fitness class training together in a bright studio"></div>
  <svg class="shards" width="753" height="560" viewBox="0 0 753 560" aria-hidden="true">
    <polygon points="0,0 150,0 0,90" fill="#9e1b1f"/>
    <polygon points="753,0 600,0 753,110" fill="#d42a2e"/>
    <polygon points="0,300 753,290 753,300" fill="#2b2b2d"/>
  </svg>
  <h2 class="goal-band"><b>87%</b> Of Out Clients Reach Their Goals !!</h2>
  <p class="blurb">Safe for moms, dads and we offer enhanced childcare with certified child care development teachers with our partner studios. Classes start at $15. Classes only available by appointment.</p>
  <address class="contact">
    <h2>CONTACT US NOW !!</h2>
    Ph: 347-555-0182<br>
    Email: Motionharbors@mailbox.example<br>
    482 Garnet Avenue, Brooklyn New York11231<br>
    www.motionharbors.example
  </address>
</section>

</body>
</html>
```